Valmorix

We need a flyer design for a new company based on Greece.

We are providing construction services on aluminum and iron constructions for houses and industrial building. On top we sell doors ( secure,wooden, aluminum).

Our initial products are based on iron and aluminum profiles We are making custom design for door, windows, stairs and in general whatever a house or and industry/factory is required.

The company is based on town center of Pireaus( the bigest port in Greece)

We would like to promote our work.
Updates

I would like to have some notes:
1. The file should be on a photo-shop, publisher or any other standard tools where changes should be possible.
2. I have some more photos that I would like to use, please let me know the method to submit

Reason: I would like to extend the dead line due to limited entries and due to my loaded schedule.

Thanks

Please all direct contacts to be through

1. gtalk, account tdraven4 at mailvex dot com or
2. MSN, account tdraven4 at postiro dot com

Thanks

Please visit the following sites:

1. http://www.kovra.gr/default.asp?siteID=1&pageID=1&langID=1, and check the logo on the left jhand side (kovra)
2. http://www.brunimo.gr/, and check the logo on the left hand side (brunimo)

You have my logo (if not request it) please try to
1. combine the logo colors in your designs and 
2. do not place the logos in the flyers, just indicate the place that could be placed.

Thanks
Stavros

Target Market(s)

landlords, legacy house owners, industries and factories, athletic groups for improving their infrastructure.

Industry/Entity Type

Construction

Requirements
Must have
• can be 2 or 4 pages folded, I can provide more photos from our projects.
Nice to have
• Security, economy from the aluminum frames
• special and professional services for the custom designs
Should not have
• old style fonts labels

```html
<!DOCTYPE html>
<html lang="en">
<head>
<meta charset="utf-8">
<title>Valmorix – Aluminium &amp; Iron Constructions</title>
<link href="https://fonts.googleapis.com/css2?family=Poppins:wght@300&display=swap" rel="stylesheet">
<style>
  :root {
    --paper: #ffffff;
    --paper-shade: #e4e4e4;
    --lime: #9cc43a;
    --lime-light: #cde27e;
    --hall-light: #f3f6f9;
    --hall-mid: #b6c0ca;
    --hall-dark: #3f4852;
    --hall-wall: #d9dee3;
    --text: #6b6b6b;
    --contact: #5c5c5c;
    --brand: #1f4fa0;
  }
  * { margin: 0; padding: 0; box-sizing: border-box; }
  html, body {
    width: 1200px; height: 847px; overflow: hidden;
    background: var(--paper);
  }
  .flyer {
    position: relative;
    width: 1200px; height: 847px;
    background: linear-gradient(to bottom, var(--paper) 0%, var(--paper) 64%, var(--paper-shade) 100%);
    font-family: "Poppins", "Century Gothic", sans-serif;
    font-weight: 300;
    color: var(--text);
  }
  .hero { position: absolute; inset: 0; }
  .brand {
    position: absolute;
    left: 30px; top: 618px;
    width: 200px;
    display: flex; flex-direction: column; align-items: center; gap: 26px;
  }
  .brand-square {
    width: 120px; height: 120px;
    background: var(--brand);
  }
  .brand-name {
    font-size: 36px;
    line-height: 1;
    color: var(--brand);
    letter-spacing: 1px;
  }
  .about {
    position: absolute;
    left: 322px; top: 600px;
    font-size: 19px;
    line-height: 30px;
    letter-spacing: 0.2px;
    white-space: nowrap;
  }
  .contacts {
    position: absolute;
    left: 322px; top: 760px;
    font-size: 25px;
    line-height: 38px;
    letter-spacing: 0.6px;
    color: var(--contact);
    white-space: nowrap;
  }
</style>
</head>
<body>
<main class="flyer">
  <svg class="hero" width="1200" height="847" viewBox="0 0 1200 847">
    <defs>
      <radialGradient id="hallLight" cx="0.55" cy="0.38" r="0.62">
        <stop offset="0" stop-color="var(--hall-light)"/>
        <stop offset="0.35" stop-color="var(--hall-mid)"/>
        <stop offset="0.75" stop-color="#6f7a86"/>
        <stop offset="1" stop-color="var(--hall-dark)"/>
      </radialGradient>
      <linearGradient id="hallFloor" x1="0" y1="0" x2="0" y2="1">
        <stop offset="0.55" stop-color="var(--hall-wall)" stop-opacity="0"/>
        <stop offset="1" stop-color="var(--hall-wall)" stop-opacity="0.8"/>
      </linearGradient>
    </defs>
    <path d="M0,122 C300,40 700,25 1200,40 L1200,62 C700,45 300,70 0,140 Z" fill="var(--lime-light)"/>
    <path d="M0,110 C320,35 720,18 1200,30 L1200,44 C720,30 320,50 0,124 Z" fill="var(--lime)"/>
    <g role="img" aria-label="Photo: interior of a steel-frame industrial hall with dark roof trusses, insulated panel walls, windows and stacked pallets">
      <path d="M0,135 C300,65 700,48 1200,58 L1200,560 C1100,500 1000,465 880,462 C650,462 300,520 0,520 Z" fill="url(#hallLight)"/>
      <path d="M0,135 C300,65 700,48 1200,58 L1200,560 C1100,500 1000,465 880,462 C650,462 300,520 0,520 Z" fill="url(#hallFloor)"/>
    </g>
    <path d="M0,520 C300,520 650,462 880,462 C1000,465 1100,500 1200,560 L1200,580 C1100,522 1000,486 880,484 C650,484 300,536 0,536 Z" fill="var(--lime)"/>
    <path d="M0,536 C300,536 650,484 880,484 C1000,486 1100,522 1200,580 L1200,596 C1100,540 1000,505 880,503 C650,503 300,548 0,548 Z" fill="var(--lime-light)"/>
  </svg>

  <div class="brand">
    <span class="brand-square"></span>
    <span class="brand-name">Valmorix</span>
  </div>

  <p class="about">We are providing construction services on aluminum and iron constructions for<br>houses and industrial building. On top we sell doors Our initial products are based<br>on iron and aluminum profiles We are making custom design for door, windows,<br>stairs and in general whatever a house or and industry/factory is required.</p>

  <div class="contacts">
    <p class="contacts-web">WEB: www.valmorix.biz, www.valmorix.com.gr</p>
    <p class="contacts-email">email: info@valmorix.biz, info@valmorix.com.gr</p>
  </div>
</main>
</body>
</html>
```